Printed Promo Flyer for new pet business

We need a double sided flyer design as per the given example flyer, just better looking and more fun.Flyers will need to be printed.Flyer size approx 10.5cm x 15cm. The text will need to be amended slightly afterwards to be more fun unless you can create a new tone of voice as well (should sound fun like brightly do it) Look and Feel: emotional, fun, loving, professional

Target Market(s)

Pet owners in the UK who want the convenience of getting their pets parasite treatment delivered to their door without the need of having to run to the vet or store for purchase

Industry/Entity Type

Pet Care

Colors
00a990
6b449b

Requirements
Must have
• all the content context as given in the example flyer.
Nice to have
• Tone of voice can be changed to be more fun (using Brightly as a guide)

```html
<!DOCTYPE html>
<html lang="en">
<head>
<meta charset="utf-8">
<title>Snug Paws Box – Flyer</title>
<link href="https://fonts.googleapis.com/css2?family=Oswald:wght@600&family=Roboto:ital,wght@0,700;1,700&family=Roboto+Condensed:wght@400;700&family=Ubuntu:wght@400;500;700&display=swap" rel="stylesheet">
<style>
  :root{
    --teal:#00a990;
    --teal-deep:#0f9c8f;
    --purple:#6b449b;
    --purple-deep:#4f1f84;
    --ink:#1d1d26;
    --yellow:#e7ef2b;
    --white:#ffffff;
    --stage:#ececef;
  }
  *{box-sizing:border-box;margin:0;padding:0}
  html,body{width:1200px;height:1200px;overflow:hidden;background:var(--stage)}
  .flyer{position:absolute;left:214px;top:48px;width:772px;height:1103px;background:var(--white);overflow:hidden;box-shadow:0 2px 10px rgba(0,0,0,.12)}
  .shapes{position:absolute;inset:0;width:772px;height:1103px}
  .brand{position:absolute;left:0;top:88px;width:380px;display:flex;align-items:center;justify-content:center;gap:12px}
  .brand-dot{width:26px;height:26px;border-radius:50%;background:var(--teal)}
  .brand-name{font-family:"Roboto",sans-serif;font-weight:700;font-size:38px;color:var(--purple);letter-spacing:1px}
  .hero-photo{position:absolute;left:370px;top:72px;width:395px;height:420px;border-radius:40% 40% 20px 20px;background:radial-gradient(ellipse at 70% 40%,#f4ead6 0%,#ead7b6 45%,#d59a5b 80%,#c98645 100%);opacity:.9}
  .headline{position:absolute;left:27px;top:240px}
  .headline-big{font-family:"Oswald",sans-serif;font-weight:600;font-size:66px;line-height:1;color:var(--purple-deep);letter-spacing:-1px}
  .headline-sub{font-family:"Roboto",sans-serif;font-weight:700;font-size:31px;line-height:34px;color:var(--teal-deep);margin-top:8px}
  .headline-with{font-family:"Roboto",sans-serif;font-style:italic;font-weight:700;font-size:27px;color:var(--purple-deep);margin-top:12px}
  .why-title{position:absolute;left:0;right:0;top:505px;text-align:center;font-family:"Roboto",sans-serif;font-weight:700;font-size:33px;color:var(--white)}
  .benefits{position:absolute;left:18px;top:560px;width:740px;display:flex}
  .benefit{flex:1;text-align:center;color:var(--white);padding:0 8px;position:relative}
  .benefit + .benefit::before{content:"";position:absolute;left:0;top:12px;height:95px;width:2px;background:rgba(255,255,255,.35)}
  .benefit-icon{width:60px;height:60px;margin:0 auto 12px;display:block}
  .benefit-title{font-family:"Ubuntu",sans-serif;font-weight:700;font-size:23px;line-height:26px}
  .benefit-text{font-family:"Ubuntu",sans-serif;font-size:14px;line-height:19px;margin-top:8px;opacity:.95}
  .offer{position:absolute;left:20px;top:792px;width:270px;height:270px;border-radius:50%;background:var(--purple-deep);border:4px solid var(--white);box-shadow:0 0 0 2px rgba(107,68,155,.25);text-align:center;color:var(--white);font-family:"Roboto Condensed",sans-serif}
  .offer-label{font-size:35px;margin-top:38px;line-height:1}
  .offer-price{font-family:"Roboto",sans-serif;font-weight:700;font-size:70px;line-height:1;color:var(--yellow);margin-top:4px}
  .offer-code{font-size:35px;line-height:1;margin-top:6px}
  .offer-box{display:inline-block;margin-top:8px;background:var(--yellow);color:#111;font-family:"Roboto",sans-serif;font-weight:700;font-size:36px;line-height:44px;padding:0 20px}
  .steps{position:absolute;right:27px;top:838px;text-align:right}
  .steps-title{font-family:"Roboto",sans-serif;font-weight:700;font-size:35px;color:var(--purple);margin-bottom:10px}
  .step{display:flex;justify-content:flex-end;align-items:flex-start;gap:10px;font-family:"Ubuntu",sans-serif;font-weight:500;font-size:18px;line-height:25px;color:var(--ink);margin-bottom:12px}
  .step-tick{width:26px;height:26px;flex:none}
  .web{position:absolute;right:0;top:1032px;width:245px;height:42px;border-radius:21px 0 0 21px;background:var(--teal);color:var(--white);font-family:"Roboto Condensed",sans-serif;font-weight:700;font-size:21px;line-height:42px;text-align:center}
</style>
</head>
<body>
<main class="flyer">
  <svg class="shapes" viewBox="0 0 772 1103" aria-hidden="true">
    <defs>
      <linearGradient id="bandFill" x1="0" y1="0" x2="1" y2="0">
        <stop offset="0" stop-color="#4f1f84"/>
        <stop offset=".5" stop-color="#6b3aa0"/>
        <stop offset="1" stop-color="#4f1f84"/>
      </linearGradient>
    </defs>
    <path d="M0 425 C260 470 520 484 690 462 C730 440 752 400 772 360 L772 520 L0 520 Z" fill="var(--teal)"/>
    <path d="M0 840 C300 770 560 768 772 800 L772 835 C560 800 300 820 0 905 Z" fill="var(--teal)"/>
    <path d="M0 440 C260 484 520 498 772 462 L772 800 C560 768 300 770 0 840 Z" fill="url(#bandFill)"/>
  </svg>

  <div class="brand">
    <span class="brand-dot"></span>
    <span class="brand-name">SNUG PAWS BOX</span>
  </div>

  <div class="hero-photo" role="img" aria-label="Photo of a ginger kitten sitting beside a cream Labrador puppy"></div>

  <section class="headline">
    <h1 class="headline-big">THE BEST</h1>
    <p class="headline-sub">PROTECTION &amp;<br>CARE FOR YOUR PET</p>
    <p class="headline-with">with SNUG PAWS BOX</p>
  </section>

  <h2 class="why-title">WHY SNUG PAWS BOX?</h2>
  <section class="benefits">
    <div class="benefit">
      <svg class="benefit-icon" viewBox="0 0 60 60"><circle cx="30" cy="30" r="30" fill="var(--teal)"/><path d="M30 14 L43 19 V30 C43 38 37 44 30 47 C23 44 17 38 17 30 V19 Z" fill="none" stroke="#fff" stroke-width="2.5"/><circle cx="30" cy="33" r="4" fill="#fff"/><circle cx="24.5" cy="27" r="2" fill="#fff"/><circle cx="30" cy="25" r="2" fill="#fff"/><circle cx="35.5" cy="27" r="2" fill="#fff"/></svg>
      <div class="benefit-title">Protection<br>&amp; Care</div>
      <p class="benefit-text">Protection against all major parasites to avoid putting your pet and your family at risk</p>
    </div>
    <div class="benefit">
      <svg class="benefit-icon" viewBox="0 0 60 60"><circle cx="30" cy="30" r="30" fill="var(--teal)"/><path d="M42 24 A14 14 0 1 1 34 17" fill="none" stroke="#fff" stroke-width="3" stroke-linecap="round"/><path d="M28 22 V31 H35" fill="none" stroke="#fff" stroke-width="3" stroke-linecap="round"/><path d="M44 14 L36 22 M36 16 V22 H42" fill="none" stroke="#fff" stroke-width="3" stroke-linecap="round"/></svg>
      <div class="benefit-title">In Time</div>
      <p class="benefit-text">Never having to remember when to treat your pet</p>
    </div>
    <div class="benefit">
      <svg class="benefit-icon" viewBox="0 0 60 60"><circle cx="30" cy="30" r="30" fill="var(--teal)"/><rect x="23" y="14" width="16" height="15" fill="#fff"/><path d="M12 38 H22 L30 41 H42 L48 36 V40 L42 46 H26 L12 44 Z" fill="#fff"/></svg>
      <div class="benefit-title">Convenient</div>
      <p class="benefit-text">Delivered directly to your letter box</p>
    </div>
    <div class="benefit">
      <svg class="benefit-icon" viewBox="0 0 60 60"><circle cx="30" cy="30" r="30" fill="var(--teal)"/><path d="M37 21 C35 18 32 17 30 17 C25 17 23 20 23 23 C23 30 37 28 37 36 C37 40 34 42 30 42 C26 42 24 40 23 38 M30 12 V48" fill="none" stroke="#fff" stroke-width="3" stroke-linecap="round"/></svg>
      <div class="benefit-title">Low cost</div>
      <p class="benefit-text">All the high end, trusted brands but cheaper than the vet</p>
    </div>
  </section>

  <div class="offer">
    <p class="offer-label">FIRST BOX</p>
    <p class="offer-price">£5.99</p>
    <p class="offer-code">USE CODE</p>
    <span class="offer-box">XXX</span>
  </div>

  <section class="steps">
    <h2 class="steps-title">HOW IT WORKS</h2>
    <p class="step"><span>Select which pet the treatment is for</span><svg class="step-tick" viewBox="0 0 26 26"><path d="M3 14 L10 21 L24 4" fill="none" stroke="var(--purple)" stroke-width="4" stroke-linecap="round" stroke-linejoin="round"/></svg></p>
    <p class="step"><span>Choose your treatment type</span><svg class="step-tick" viewBox="0 0 26 26"><path d="M3 14 L10 21 L24 4" fill="none" stroke="var(--purple)" stroke-width="4" stroke-linecap="round" stroke-linejoin="round"/></svg></p>
    <p class="step"><span>Select your preferred brand Choose between<br>1, 3, 6 or 12 months treatment</span><svg class="step-tick" viewBox="0 0 26 26"><path d="M3 14 L10 21 L24 4" fill="none" stroke="var(--purple)" stroke-width="4" stroke-linecap="round" stroke-linejoin="round"/></svg></p>
  </section>

  <div class="web">www.snugpawsbox.co.uk</div>
</main>
</body>
</html>
```